Business Card Design

We are a commercial real estate brokerage in San Francisco, leasing office buildings downtown.
I would like a clean, elegant look. Simple but powerful .

Industry/Entity Type

Business

Contact Information for Business Card

Derek Hollings
lic# 02875140
415.287.6041
derek@vexa-commercial.com
vexa-commercial.com

```html
<!DOCTYPE html>
<html lang="en">
<head>
<meta charset="utf-8">
<title>VEXA Commercial – Business Cards</title>
<link href="https://fonts.googleapis.com/css2?family=Open+Sans:wght@400;600&display=swap" rel="stylesheet">
<style>
  :root {
    --page: #e9e7e3;
    --card: #ffffff;
    --band-dark: #6f6f6f;
    --band-light: #a3a3a3;
    --accent: #7f93b3;
    --ink: #5a5a5a;
    --on-band: #ffffff;
  }
  * { margin: 0; padding: 0; box-sizing: border-box; }
  html, body { width: 1200px; height: 950px; overflow: hidden; }
  body {
    background: var(--page);
    font-family: "Open Sans", sans-serif;
    position: relative;
  }
  .card {
    position: absolute;
    left: 220px;
    width: 760px;
    height: 434px;
    background: var(--card);
    box-shadow: 0 6px 18px rgba(0,0,0,.18);
    overflow: hidden;
  }
  .card--front { top: 26px; }
  .card--back { top: 490px; }

  .brand {
    position: absolute;
    display: flex;
    align-items: center;
    gap: 14px;
  }
  .brand__mark {
    width: 44px; height: 44px;
    background: var(--accent);
  }
  .brand__name {
    color: var(--accent);
    font-weight: 600;
    line-height: 1;
  }
  .brand__name .line1 { display: block; font-size: 40px; letter-spacing: 1px; }
  .brand__name .line2 { display: block; font-size: 16px; letter-spacing: 2px; margin-top: 2px; }
  .card--front .brand { left: 300px; top: 52px; }
  .card--back .brand { left: 390px; top: 72px; }

  .band {
    position: absolute;
    background: linear-gradient(100deg, var(--band-dark), var(--band-light));
  }
  .card--front .band { left: 0; right: 0; top: 150px; height: 170px; }
  .tagline {
    position: absolute; inset: 0;
    display: flex; flex-direction: column; justify-content: center; align-items: center;
    color: var(--on-band);
    font-size: 17px;
    line-height: 1.5;
    text-align: center;
  }

  .card--back .band { left: 390px; right: 0; top: 190px; height: 130px; }
  .contacts {
    list-style: none;
    position: absolute;
    left: 36px; top: 24px;
    color: var(--on-band);
    font-size: 17px;
  }
  .contacts li { display: flex; align-items: center; gap: 10px; line-height: 27px; }
  .contacts svg { width: 15px; height: 15px; fill: var(--on-band); flex: none; }

  .accent-bar {
    position: absolute;
    left: 0; bottom: 0;
    width: 14px; height: 130px;
    background: var(--accent);
  }
  .holder {
    position: absolute;
    left: 40px; top: 318px;
  }
  .holder__name { color: var(--accent); font-weight: 600; font-size: 26px; }
  .holder__licence { color: var(--ink); font-size: 17px; margin-top: 2px; }
</style>
</head>
<body>

<section class="card card--front">
  <div class="brand">
    <span class="brand__mark"></span>
    <span class="brand__name"><span class="line1">VEXA</span><span class="line2">COMMERCIAL</span></span>
  </div>
  <div class="band">
    <p class="tagline">
      <span>commercial real estate brokerage in San Francisco</span>
      <span>leasing office buildings downtown.</span>
    </p>
  </div>
</section>

<section class="card card--back">
  <div class="brand">
    <span class="brand__mark"></span>
    <span class="brand__name"><span class="line1">VEXA</span><span class="line2">COMMERCIAL</span></span>
  </div>
  <div class="band">
    <ul class="contacts">
      <li>
        <svg viewBox="0 0 24 24" aria-hidden="true"><path d="M6.6 10.8a15.1 15.1 0 0 0 6.6 6.6l2.2-2.2c.3-.3.7-.4 1-.2 1.1.4 2.3.6 3.6.6.6 0 1 .4 1 1V20c0 .6-.4 1-1 1A17 17 0 0 1 3 4c0-.6.4-1 1-1h3.5c.6 0 1 .4 1 1 0 1.3.2 2.5.6 3.6.1.3 0 .7-.2 1z"/></svg>
        415.287.6041
      </li>
      <li>
        <svg viewBox="0 0 24 24" aria-hidden="true"><path d="M2 5h20v14H2z M3.5 6.5 12 13l8.5-6.5" fill="none" stroke="#fff" stroke-width="2"/></svg>
        derek@vexa-commercial.com
      </li>
      <li>
        <svg viewBox="0 0 24 24" aria-hidden="true"><circle cx="12" cy="12" r="9" fill="none" stroke="#fff" stroke-width="2"/><path d="M3 12h18M12 3c3 3 3 15 0 18M12 3c-3 3-3 15 0 18" fill="none" stroke="#fff" stroke-width="1.6"/></svg>
        vexa-commercial.com
      </li>
    </ul>
  </div>
  <span class="accent-bar"></span>
  <div class="holder">
    <p class="holder__name">Derek Hollings</p>
    <p class="holder__licence">lic# 02875140</p>
  </div>
</section>

</body>
</html>
```